Eco friendly Swedish beauty products sold in aluminum bottles - label design needed

We need help in designing a series of stick on labels for 80 ml (2.7 fl. oz.) aluminum bottles containing beauty products such as soaps, shampoo etc. The diameter of the bottle is 36 mm and the body of the bottles measures approx. 106 mm.
It is important for us that the label has a simplistic and clean feel with few colors (and the right ones!) and that the label helps amplify this product being both better and a more sustainable alternative to many of our plastic bottle competitors. The design and label should communicate the feel of an Eco-friendly, sustainable and modern brand of high quality - and with a Swedish concept.
We are using Montserrat font in our materials. Find attached information of preferred colors, the bottles and one example of our logotype. I am also available on e-mail should further information be needed.

Looking forward and very excited to receive your suggestions.
Note that we are expecting to start selling a series of approximately 10 different products where I will need one "master design" and then only smaller changes for each of the different products.

Target Market(s)

People whom are aware and not only look at price tag. Private and commercial market.

Industry/Entity Type

Beauty

Font styles to use
Other font styles liked:
• Montserrat

Requirements
Must have
• It must give the feel of being both better and a more sustainable alternative to many of our plastic bottle competitors.
Nice to have
• Simplistic. Clean. Clear.
Should not have
• Wrong colors, too complex designs.

```html
<!DOCTYPE html>
<html lang="en">
<head>
<meta charset="utf-8">
<title>Label series – hand soap and hand sanitizer</title>
<link rel="stylesheet" href="https://fonts.googleapis.com/css2?family=Jost:wght@300;400;600&display=swap">
<style>
  :root {
    --moss: #6e7838;
    --stone: #e0dedb;
    --stone-text: #dedcd7;
    --page: #ffffff;
  }
  html, body {
    margin: 0;
    width: 1200px;
    height: 1200px;
    overflow: hidden;
    background: var(--page);
  }
  .canvas {
    position: relative;
    width: 1200px;
    height: 1200px;
    font-family: 'Jost', 'Futura', sans-serif;
  }
  .label {
    position: absolute;
    top: 52px;
    width: 372px;
    height: 1095px;
  }
  .label--soap { left: 215px; background: var(--moss); color: var(--stone-text); }
  .label--sanitizer { left: 614px; background: var(--stone); color: var(--moss); }
  .brand-name {
    position: absolute;
    left: 57px;
    top: 58px;
    margin: 0;
    font-weight: 300;
    font-size: 40px;
    line-height: 1;
    letter-spacing: 6px;
  }
  .product-name {
    position: absolute;
    left: 57px;
    top: 790px;
    margin: 0;
    font-weight: 600;
    font-size: 47px;
    line-height: 52px;
    letter-spacing: 1.5px;
  }
  .skin-type {
    position: absolute;
    left: 58px;
    top: 915px;
    margin: 0;
    font-weight: 300;
    font-size: 23.5px;
  }
  .volume {
    position: absolute;
    left: 58px;
    top: 1026px;
    margin: 0;
    font-weight: 400;
    font-size: 19px;
  }
</style>
</head>
<body>
<main class="canvas">
  <section class="label label--soap">
    <p class="brand-name">NORRVIK</p>
    <h2 class="product-name">hand<br>soap</h2>
    <p class="skin-type">for sensitive skin</p>
    <p class="volume">80ml (2.7 fl. oz.)</p>
  </section>

  <section class="label label--sanitizer">
    <p class="brand-name">NORRVIK</p>
    <h2 class="product-name">hand<br>sanitizer</h2>
    <p class="skin-type">for sensitive skin</p>
    <p class="volume">80ml (2.7 fl. oz.)</p>
  </section>
</main>
</body>
</html>
```